Business Card Design

Industry/Entity Type

Business

Contact Information for Business Card

I have attached images of previously designed business card from pixel harbor.
All I am after this time is for some of the information to be edited.
My new contact details are:
382 Barrow Creek Rd, Wyndale
Kestrel Vale 3519
Mob: +61 (0) 455 318 207
Home: +61 03 5291 4083
dean@marlowfieldthoroughbreds.com

New Details in the information at the top is:
Racehorse Spelling
Broodmare Agistment
Sales Preparation
Breaking
Bloodstock Consultancy

```html
<!DOCTYPE html>
<html lang="en">
<head>
<meta charset="utf-8">
<title>Marlowfield Thoroughbreds – Business Card</title>
<link href="https://fonts.googleapis.com/css2?family=Arimo:wght@400;700&display=swap" rel="stylesheet">
<style>
  :root {
    --stage: #e9eaee;
    --card-white: #ffffff;
    --card-blue: #2f8fd8;
    --brand-grey: #6f7378;
    --text-grey: #7a7e84;
    --rule: #cfd2d6;
    --accent: #1f5f9e;
    --on-blue: #e8f3fc;
  }
  * { box-sizing: border-box; margin: 0; padding: 0; }
  html, body {
    width: 1200px; height: 901px; overflow: hidden;
    background: var(--stage);
    font-family: "Arimo", Arial, sans-serif;
  }
  .stage { position: relative; width: 1200px; height: 901px; }

  .card {
    position: absolute;
    border-radius: 22px;
    box-shadow: 0 6px 18px rgba(0,0,0,.12);
  }

  /* Front: portrait, white */
  .card-front {
    left: 130px; top: 172px; width: 340px; height: 556px;
    background: var(--card-white);
    padding: 48px 36px 0;
    color: var(--text-grey);
  }
  .brand-name {
    text-align: center;
    color: var(--brand-grey);
    font-weight: 400;
    font-size: 19px;
    letter-spacing: 6px;
    line-height: 1.45;
  }
  .rule { height: 1px; background: var(--rule); margin: 34px 0 28px; }
  .services { list-style: none; font-size: 14px; line-height: 1.45; padding-left: 18px; }
  .services li { position: relative; padding-left: 14px; }
  .services li::before {
    content: ""; position: absolute; left: 0; top: 5px;
    width: 7px; height: 7px; background: var(--accent);
  }
  .person {
    color: var(--accent); font-weight: 700; font-size: 22px;
    text-align: center; margin-bottom: 26px;
  }
  .contact { list-style: none; font-size: 11.5px; line-height: 1.35; }
  .contact li { display: flex; align-items: flex-start; gap: 10px; margin-bottom: 7px; }
  .contact svg { flex: none; width: 16px; height: 16px; fill: var(--accent); margin-top: -1px; }

  /* Back: landscape, blue */
  .card-back {
    left: 540px; top: 280px; width: 556px; height: 340px;
    background: var(--card-blue);
    display: flex; align-items: center; justify-content: center;
  }
  .card-back .brand-name {
    color: var(--on-blue);
    font-size: 30px; letter-spacing: 12px; line-height: 1.5;
  }
</style>
</head>
<body>
<main class="stage">

  <section class="card card-front" aria-label="Business card front">
    <h1 class="brand-name">MARLOWFIELD<br>THOROUGHBREDS</h1>
    <div class="rule"></div>
    <ul class="services">
      <li>Racehorse Spelling</li>
      <li>Broodmare Agistment</li>
      <li>Sales Preparation</li>
      <li>Breaking</li>
      <li>Bloodstock Consultancy</li>
    </ul>
    <div class="rule"></div>
    <p class="person">Dean Holloway</p>
    <ul class="contact">
      <li>
        <svg viewBox="0 0 16 16" aria-hidden="true"><path d="M5 1h6a1 1 0 0 1 1 1v12a1 1 0 0 1-1 1H5a1 1 0 0 1-1-1V2a1 1 0 0 1 1-1zm0 2v9h6V3zm3 10a.8.8 0 1 0 0 .01z"/></svg>
        <span>+61 (0) 455 318 207</span>
      </li>
      <li>
        <svg viewBox="0 0 16 16" aria-hidden="true"><path d="M3 2l3 0 1 3-2 1.5a8 8 0 0 0 4.5 4.5L11 9l3 1v3a1 1 0 0 1-1 1A11 11 0 0 1 2 3a1 1 0 0 1 1-1z"/></svg>
        <span>+61 03 5291 4083</span>
      </li>
      <li>
        <svg viewBox="0 0 16 16" aria-hidden="true"><path d="M1 4h14v9H1zm1.5 1.2v.3L8 9.2l5.5-3.7v-.3zm0 1.9V12h11V7.1L8 10.8z"/></svg>
        <span>382 Barrow Creek Rd,<br>Wyndale Kestrel Vale 3519</span>
      </li>
      <li>
        <svg viewBox="0 0 16 16" aria-hidden="true"><path d="M8 1l7 6.5h-2V15H9.5v-4h-3v4H3V7.5H1z"/></svg>
        <span>dean@marlowfieldthoroughbreds.com</span>
      </li>
    </ul>
  </section>

  <section class="card card-back" aria-label="Business card back">
    <p class="brand-name">MARLOWFIELD<br>THOROUGHBREDS</p>
  </section>

</main>
</body>
</html>
```